Brochure Design Project A5 (UK) 64 pages apox Making Money From Financial Trading

I require a website (long sales letter) turned into a A5 booklet for mailing out will will be full colour. You must provide a complete end to end to service, I will provide all the text and photos and you need to layout and design the brochure, resize photos to fit. I see the size being around 64 sides of UK A5 paper
148 x 210mm 5.83 x 8.27

You must be creative with text layout and typography, this is very text heavy over 10,000 words in to total. the website can be seen at www.brassfold-ledger.com however this is NOT the final text but gives you an idea. (I have attached 5 pages of text)

They typical reader is male over 40, it needs to be readable, experience with magazine layouts and advantage

The finished project must be ready to go to print.

So it needs a front and back cover designed - I have attached a sample DVD cover as an idea from one of our products and then the inside pages, designed/set out
Updates

We have made the project guaranteed so step up and give me your best designs

Reason: Dear All. The standard of work submitted so far has been very poor and amateurish. We have decided to use another company for the front and back cover, therefore leaving you to concentrate on the text for inside the booklet. If you wish to resubmit some better designs then please go ahead. Thx

Target Market(s)

The typical client is Male, professional, looking make money from the stockmarket. The end user already knows the author

Industry/Entity Type

Financial

Requirements
Must have
• Must have good and creative typography

```html
<!DOCTYPE html>
<html lang="en">
<head>
<meta charset="utf-8">
<title>Booklet spread – page 9</title>
<link rel="stylesheet" href="https://fonts.googleapis.com/css2?family=Tinos:ital,wght@0,400;0,700;1,400&family=Oswald:wght@600&family=Arimo:ital,wght@1,700&display=swap">
<style>
  :root {
    --paper: #ffffff;
    --facing-page: #bcbcbe;
    --ink: #1a1a1a;
    --accent-blue: #00a6e9;
    --frame: #000000;
  }
  * { margin: 0; padding: 0; box-sizing: border-box; }
  html, body {
    width: 1200px;
    height: 851px;
    overflow: hidden;
    background: var(--paper);
  }
  .spread {
    position: relative;
    width: 1200px;
    height: 851px;
  }
  .page-left {
    position: absolute;
    left: 0; top: 0;
    width: 600px; height: 851px;
    background: var(--paper);
    border: 1.5px solid var(--frame);
  }
  .page-right {
    position: absolute;
    left: 600px; top: 0;
    width: 600px; height: 851px;
    background: var(--facing-page);
  }
  .folio {
    position: absolute;
    left: 39px; top: 16px;
    font-family: "Arimo", Arial, sans-serif;
    font-style: normal;
    font-weight: 700;
    font-size: 15px;
    color: var(--ink);
  }
  .header-rule {
    position: absolute;
    left: 40px; top: 140px;
    width: 560px; height: 12px;
    background: var(--accent-blue);
  }
  .body-column {
    position: absolute;
    top: 157px;
    width: 231px;
    font-family: "Tinos", "Times New Roman", serif;
    font-size: 15.6px;
    line-height: 21px;
    color: var(--ink);
    text-align: justify;
    hyphens: none;
  }
  .body-column p + p { margin-top: 21px; }
  .column-one { left: 40px; }
  .column-two { left: 307px; width: 229px; }
  .body-column em { font-style: italic; }
  .body-column strong { font-weight: 700; }
  .headline {
    position: absolute;
    left: 307px;
    font-family: "Oswald", "Arial Narrow", sans-serif;
    font-weight: 600;
    font-size: 45px;
    line-height: 46px;
    color: var(--accent-blue);
    text-transform: uppercase;
    letter-spacing: -0.2px;
  }
  .headline-experience { top: 262px; }
  .headline-job { top: 465px; }
  .lead-question {
    position: absolute;
    left: 307px; top: 396px;
    width: 229px;
    font-family: "Arimo", Arial, sans-serif;
    font-style: italic;
    font-weight: 700;
    font-size: 18px;
    line-height: 25px;
    color: var(--ink);
  }
  .aside-note {
    position: absolute;
    left: 307px; top: 514px;
    width: 229px;
    font-family: "Tinos", "Times New Roman", serif;
    font-style: italic;
    font-size: 15px;
    line-height: 19px;
    color: var(--ink);
  }
</style>
</head>
<body>
<main class="spread">
  <section class="page-left">
    <span class="folio">9</span>
    <div class="header-rule"></div>

    <div class="body-column column-one">
      <p>business channels, but the truth is, most of them don’t have a pot to piss in. The may manage billions of other people’s money, but they have no skin in the game.</p>
      <p>I don’t take a penny of investment capital from anyone else, I genuinely trade and invest my own account(s) and I <em>“eat my own cooking”</em>.</p>
      <p>Would you like to be my Private Student for the next 12 months and trade alongside me from the comfort of your home? Would you like me to show you how to earn a very large <strong>INCOME</strong> from Financial Trading and trading other financial products using this system … a system which I’ve used and perfected over the last ten years and which I’ve personally used to average over <strong>£24,900 PER WEEK?</strong></p>
      <p>Would you like me to be your Personal Mentor? If you do, you’ll need access to the Internet … and about 20-30 minutes spare each day to follow some simple steps.</p>
    </div>

    <div class="body-column column-two">
      <p>And don’t worry if you know little or nothing about Internet Financial Trading. <em>You’ll need absolutely…</em></p>
    </div>

    <h2 class="headline headline-experience">No<br>Experience</h2>
    <p class="lead-question">How would you like this job description?</p>
    <h2 class="headline headline-job">No Job</h2>
    <p class="aside-note">(that’s a great Job description in itself).</p>
  </section>

  <section class="page-right" aria-hidden="true"></section>
</main>
</body>
</html>
```